Velmor Haulage Heavy Goods Transport web design

I have a client who requires a new web site design.
They are Velmor Haulage in the UK.
They have a current site which needs updating with a fresh look and feel using modern design ideas.
Their current site is velmorhaulage.co.uk
I will use your design to build a new CMS site for them using Django.
I only require the layered PSD files, main page design plus a sub page showing navigation changes and layout changes between pages.
The site needs to have the same sections as the current site plus:
1) Proof of delivery downloads system (customer logs in to access their delivery documents).
2) CMS system will allow them to add pages so the menu system needs to be designed such that it can expand.
3) A contact page with a contact form and a Google map will be used.
4) No flash.
5) Slideshow banners (using JQuery will be used).
I like the following type of designs:
www.billotrix.com/pricing.html
www.ledgerpine.com/
quorvel.ly/features
tabnestix.com/
I am looking for a designer to work with me designing other web design projects as well so this project will be used as a test bed for us working together.
The budget for our client designs is between £120 and £200 depending on functionality requirements. This site has a budget of £150.
Please submit your quotes by email to dharlow@brenquay.com
Industrial business customers
Build

```html
<!DOCTYPE html>
<html lang="en">
<head>
<meta charset="utf-8">
<title>Velmor Haulage – Heavy Goods Transport</title>
<link rel="stylesheet" href="https://fonts.googleapis.com/css2?family=Arimo:wght@400;700&display=swap">
<style>
  :root {
    --blue: #00adef;
    --blue-heading: #1aa6e0;
    --red-phone: #e8141b;
    --text: #3c3c3c;
    --muted: #7a7a7a;
    --yellow: #fff04a;
    --red: #ec1c24;
    --green: #2ecf2e;
    --white: #ffffff;
    --hero-top: #8fd0d8;
    --hero-bottom: #102a4a;
  }
  * { box-sizing: border-box; margin: 0; padding: 0; }
  html, body { width: 1062px; height: 1200px; overflow: hidden; background: var(--white); }
  body { font-family: "Arimo", Arial, sans-serif; color: var(--text); position: relative; }

  .site-header { position: absolute; left: 0; top: 0; width: 1062px; height: 80px; }
  .brand { position: absolute; left: 18px; top: 40px; font-size: 21px; letter-spacing: 0.3px; color: #333; white-space: nowrap; }
  .phone { position: absolute; right: 32px; top: 43px; font-size: 17px; color: var(--red-phone); text-shadow: 1px 2px 3px rgba(0,0,0,.25); white-space: nowrap; }

  .main-nav { position: absolute; left: 0; top: 80px; width: 1047px; height: 47px; background: var(--blue); display: flex; }
  .main-nav a { color: var(--white); text-decoration: none; font-size: 13.5px; display: flex; align-items: center; justify-content: center; border-right: 1px solid rgba(255,255,255,.35); height: 100%; white-space: nowrap; }
  .main-nav a.nav-email { border-right: 0; font-size: 11.5px; letter-spacing: -0.1px; }

  .hero { position: absolute; left: 0; top: 139px; width: 1042px; height: 410px; box-shadow: 3px 3px 6px rgba(0,0,0,.35); overflow: hidden; }
  .hero-image { position: absolute; inset: 0; background: linear-gradient(180deg, var(--hero-top) 0%, #3d7c95 35%, #1c3e62 65%, var(--hero-bottom) 100%); }
  .hero-lead { position: absolute; left: 16px; top: 66px; width: 500px; font-size: 21px; line-height: 30px; color: var(--white); }
  .hero-card { position: absolute; top: 281px; width: 243px; height: 105px; background: rgba(90,90,95,.75); color: var(--white); padding: 18px 9px; }
  .hero-card h3 { font-weight: 400; font-size: 15.5px; margin-bottom: 12px; white-space: nowrap; }
  .hero-card p { font-size: 12px; line-height: 18px; width: 170px; letter-spacing: -0.2px; }
  .hero-card .icon { position: absolute; left: 180px; top: 46px; width: 72px; height: 54px; border-radius: 6px; }
  .card-one { left: 18px; }
  .card-two { left: 300px; }

  .intro { position: absolute; left: 16px; top: 585px; width: 1014px; }
  .intro h1 { font-weight: 400; font-size: 20px; color: var(--blue-heading); margin-bottom: 18px; }
  .intro p { font-size: 15.5px; line-height: 20px; text-align: justify; color: #555; }

  .feature { position: absolute; top: 762px; width: 320px; height: 226px; background: var(--white); box-shadow: 2px 3px 5px rgba(0,0,0,.3); padding: 7px; }
  .feature-inner { position: relative; width: 100%; height: 100%; padding: 22px 18px; }
  .feature h2 { font-weight: 400; font-size: 18px; margin-bottom: 8px; color: #111; }
  .feature p { font-size: 11px; line-height: 15px; width: 222px; text-align: justify; color: #111; }
  .learn-more { display: block; margin-top: 17px; width: 139px; height: 21px; border-radius: 11px; background: var(--white); font-size: 11px; line-height: 21px; padding-left: 15px; color: #111; text-decoration: none; }
  .feature .illus { position: absolute; right: 16px; bottom: 10px; width: 80px; height: 70px; border-radius: 8px; }
  .culture { left: 16px; } .culture .feature-inner { background: var(--yellow); }
  .team { left: 368px; } .team .feature-inner { background: var(--red); }
  .social { left: 717px; } .social .feature-inner { background: var(--green); }
  .social blockquote { position: absolute; left: 30px; top: 58px; width: 222px; font-size: 11px; line-height: 15px; color: var(--white); }
  .follow { position: absolute; right: 18px; bottom: 16px; width: 118px; height: 46px; background: #1a5fc2; color: var(--white); font-size: 12px; font-weight: 700; display: flex; align-items: center; justify-content: center; border-radius: 4px; text-decoration: none; }

  .divider { position: absolute; left: 14px; top: 1050px; width: 1034px; height: 8px; box-shadow: 0 -4px 8px rgba(0,0,0,.06); }
  .site-footer { position: absolute; left: 0; top: 1080px; width: 1062px; font-size: 10.5px; line-height: 14px; color: var(--muted); }
  .footer-address { position: absolute; left: 34px; top: 0; }
  .footer-contact { position: absolute; left: 34px; top: 74px; }
  .footer-contact .tel { color: #5aa6d8; }
  .footer-contact .mail { color: #f07a7a; }
  .copyright { position: absolute; left: 868px; top: 8px; white-space: nowrap; }
</style>
</head>
<body>
  <header class="site-header">
    <div class="brand">VELMOR HAULAGE.CO.UK</div>
    <div class="phone">Telephone 01632 960418</div>
  </header>

  <nav class="main-nav">
    <a href="#" style="width:93px">welcome</a>
    <a href="#" style="width:112px">introduction</a>
    <a href="#" style="width:84px">culture</a>
    <a href="#" style="width:95px">the team</a>
    <a href="#" style="width:80px">depots</a>
    <a href="#" style="width:128px">contact details</a>
    <a href="#" style="width:115px">notice board</a>
    <a href="#" style="width:145px">customer feedback</a>
    <a href="#" class="nav-email" style="width:195px">E:Mail info@velmorhaulage.co.uk</a>
  </nav>

  <section class="hero">
    <div class="hero-image" role="img" aria-label="Photograph of a white articulated lorry driving on an open road at dusk under a blue sky"></div>
    <p class="hero-lead">Nullam condimentum diam eu eros pretium posuere. Nullam ac justo ut odio vestibulum volutpat. Praesent nec consequat elit.</p>
    <div class="hero-card card-one">
      <h3>NULLAM CONDIMENTUM</h3>
      <p>Driver hire – This is a perfect option to get you to the airport.</p>
      <div class="icon" role="img" aria-label="Illustration of a small green lorry" style="background:linear-gradient(135deg,#4fd23e,#1e8f1e)"></div>
    </div>
    <div class="hero-card card-two">
      <h3>NULLAM CONDIMENTUM</h3>
      <p>Driver hire – This is a perfect option to get you to the airport.</p>
      <div class="icon" role="img" aria-label="Illustration of a small orange lorry" style="background:linear-gradient(135deg,#ffcf3a,#f08a10)"></div>
    </div>
  </section>

  <section class="intro">
    <h1>Quisque id erat mattis diam consectetur fermentum non eu purus.</h1>
    <p>Morbi aliquet, libero ac pellentesque dapibus, mi enim sollicitudin mi, quis volutpat mi ante nec purus. Donec ut mi velit. Etiam facilisis faucibus elit, id hendrerit augue tincidunt ut. Nulla bibendum nunc non purus egestas id cursus massa rutrum. Suspendisse potenti. Etiam consequat vulputate consectetur. Fusce hendrerit sollicitudin consectetur. Aliquam iaculis consequat dapibus. Suspendisse potenti. Pellentesque habitant morbi tristique senectus et netus et malesuada fames ac turpis egestas. Aliquam at dolor turpis, id ultricies eros.</p>
  </section>

  <article class="feature culture">
    <div class="feature-inner">
      <h2>Our Culture</h2>
      <p>Morbi aliquet, libero ac pellentesque dapibus, mi enim sollicitudin mi, quis volutpat mi ante nec purus. Donec ut mi velit. Etiam facilisis faucibus elit, id hendrerit augue tincidunt ut.</p>
      <a href="#" class="learn-more">learn more</a>
      <div class="illus" role="img" aria-label="Illustration of a crossed spanner and hammer" style="width:66px;height:66px;background:linear-gradient(135deg,#d8d8d0,#8a8a80)"></div>
    </div>
  </article>

  <article class="feature team">
    <div class="feature-inner">
      <h2>Our Team</h2>
      <p>Morbi aliquet, libero ac pellentesque dapibus, mi enim sollicitudin mi, quis volutpat mi ante nec purus. Donec ut mi velit. Etiam facilisis faucibus elit, id hendrerit augue tincidunt ut.</p>
      <a href="#" class="learn-more">learn more</a>
      <div class="illus" role="img" aria-label="Illustration of a black lorry carrying an orange parcel" style="width:96px;height:70px;background:linear-gradient(160deg,#f0a040,#2a2a2a)"></div>
    </div>
  </article>

  <article class="feature social">
    <div class="feature-inner">
      <blockquote>“ Morbi aliquet, libero ac pellentesque dapibus, mi enim sollicitudin mi, quis volutpat mi ante nec purus. Donec ut mi velit. Etiam facilisis faucibus elit, id hendrerit augue tincidunt ut. ”</blockquote>
      <a href="#" class="follow">Follow Me</a>
    </div>
  </article>

  <div class="divider"></div>

  <footer class="site-footer">
    <div class="footer-address">
      Velmor Haulage Services (Midlands) Limited<br>
      Brookfield Yard, Mill Lane,<br>
      Ashby Moor, Nr Fenwick, Harlowby,<br>
      HB4 2QT
    </div>
    <div class="footer-contact">
      <span class="tel">Telephone 01632 960418,&nbsp; Fax 01632 960427</span><br>
      <span class="mail">E:Mail info@velmorhaulage.co.uk</span>
    </div>
    <div class="copyright">
      © Copyright 2012<br>
      Velmor Haulage Services (Midlands)<br>
      All rights reserved
    </div>
  </footer>
</body>
</html>
```